Brochure Design

We are looking for a brochure design that describes our credit repair and restoration business.
One of the files that has been uploaded is "TRV Presentation Guidebook". This provides information about our service and snippets can be used for the text in the brochure.
I also uploaded several examples of brochures that we liked.
Target Market(s)
The target market is consumers, not businesses, who are considering our credit repair and restoration service.
Industry/Entity Type
Business
Requirements
Must have
- We want a brochure that is rich with color, and pictures of families and business people. Large pictures that span the entire length of the brochure, or several panels is preferred. The color scheme should be black and blue based
Nice to have
- A stylized representation of our logo. Our logo is not important to be included in the primary design scheme, because our logo is not stylistic enough from what we currently have. However, a stylized version of our logo that can be integrated into the design in some way would be wonderful. We will attached a pic of our design. It is pretty basic and there are many stock photos or art that can be used to offer a more stylized version of our logo to incorporate into the design.
Should not have
- The primary focus of the brochure is a professional design with plenty of color and pictures. This is not designed to necessarily be an informative brochure, but more of a "business presence" brochure. So there is not a need to provide a lot of space for text. Certainly there should be enough text to describe our business and make some bullet points, but text explanation is not the focus.

```html
<!DOCTYPE html>
<html lang="en">
<head>
<meta charset="utf-8">
<title>TRV Credit Brochure</title>
<link rel="stylesheet" href="https://fonts.googleapis.com/css2?family=Open+Sans:wght@400;600;700&display=swap">
<style>
  :root {
    --page: #ffffff;
    --teal: #3aaca6;
    --teal-light: #5cc2bc;
    --slate: #566a68;
    --ink: #111111;
    --gold: #f5c518;
    --white: #ffffff;
  }
  * { box-sizing: border-box; margin: 0; padding: 0; }
  html, body {
    width: 1200px; height: 985px; overflow: hidden;
    background: var(--page);
    font-family: "Open Sans", Arial, sans-serif;
  }
  .canvas { position: relative; width: 1200px; height: 985px; }

  .side-label {
    position: absolute; top: 812px;
    font-size: 34px; font-weight: 400; color: var(--ink);
  }
  .side-label--a { left: 22px; }
  .side-label--b { left: 1070px; }

  .panel {
    position: absolute; top: 65px;
    width: 420px; height: 880px; overflow: hidden;
    background: var(--white);
    box-shadow: 0 2px 10px rgba(0,0,0,.18);
  }
  .panel--front { left: 180px; }
  .panel--inside { left: 640px; }

  .photo { position: absolute; left: 0; width: 100%; }
  .photo-word {
    position: absolute; top: -14px; left: 2px;
    font-size: 100px; font-weight: 700; letter-spacing: -2px;
    color: rgba(235,235,235,.55); line-height: 1;
  }

  /* Front panel */
  .panel--front .photo {
    top: 0; height: 320px;
    background:
      radial-gradient(ellipse 95px 110px at 285px 225px, rgba(225,225,225,.85), rgba(225,225,225,0) 100%),
      radial-gradient(ellipse 90px 120px at 190px 240px, rgba(190,190,190,.75), rgba(190,190,190,0) 100%),
      radial-gradient(ellipse 160px 170px at 250px 250px, rgba(25,25,25,.9), rgba(25,25,25,0) 100%),
      linear-gradient(180deg, #8d8d8d 0%, #5c5c5c 45%, #3b3b3b 100%);
  }
  .hero-band {
    position: absolute; top: 320px; left: 0; width: 100%; height: 315px;
    background: linear-gradient(160deg, var(--teal-light), var(--teal));
    padding: 4px 20px 0 26px;
  }
  .hero-bars { position: absolute; inset: 0; }
  .hero-text { position: relative; }
  .hero-band .big { font-size: 88px; font-weight: 600; color: var(--white); line-height: 1; }
  .hero-band .line { font-size: 41px; font-weight: 600; color: var(--ink); line-height: 1.05; }
  .hero-band .small { font-size: 27px; font-weight: 600; color: var(--ink); margin-top: 22px; line-height: 1.05; }
  .hero-band .gold { font-size: 35px; font-weight: 600; color: var(--gold); line-height: 1.05; }
  .hero-band .end { font-size: 86px; font-weight: 600; color: var(--white); line-height: .95; text-align: right; padding-right: 44px; }

  .brand {
    position: absolute; top: 635px; left: 0; width: 100%; height: 120px;
    display: flex; flex-direction: column; align-items: center; justify-content: center; gap: 4px;
  }
  .brand-row { display: flex; align-items: center; gap: 12px; }
  .brand-mark { width: 30px; height: 30px; background: var(--teal); }
  .brand-name { font-size: 34px; font-weight: 700; color: var(--teal); }
  .brand-tagline { font-size: 11px; font-weight: 700; color: var(--slate); letter-spacing: .5px; text-transform: uppercase; }

  .contact-band {
    position: absolute; top: 755px; left: 0; width: 100%; height: 95px;
    background: var(--slate); color: var(--white);
    font-style: normal; font-size: 11px; font-weight: 700; line-height: 1.5;
    text-align: center; padding-top: 20px;
  }

  /* Inside panel */
  .message-band {
    position: absolute; top: 0; left: 0; width: 100%; height: 320px;
    background: var(--slate); padding: 20px 24px 0 24px;
  }
  .message-band .lead { font-size: 43px; font-weight: 600; color: var(--white); line-height: 1.05; }
  .message-band .strong { font-size: 68px; font-weight: 700; color: var(--ink); line-height: 1; }
  .message-band .gold { font-size: 42px; font-weight: 600; color: var(--gold); line-height: 1.05; padding-left: 48px; }
  .message-band .dark { font-size: 36px; font-weight: 600; color: var(--ink); line-height: 1.05; padding-left: 70px; }
  .message-band .end { font-size: 84px; font-weight: 600; color: var(--white); line-height: .95; text-align: right; }
  .panel--inside .photo {
    top: 320px; height: 560px;
    background:
      radial-gradient(ellipse 110px 140px at 160px 300px, rgba(235,235,235,.9), rgba(235,235,235,0) 100%),
      radial-gradient(ellipse 120px 220px at 85px 400px, rgba(245,245,245,.85), rgba(245,245,245,0) 100%),
      radial-gradient(ellipse 140px 330px at 345px 380px, rgba(40,40,40,.95), rgba(40,40,40,0) 100%),
      radial-gradient(ellipse 80px 120px at 30px 200px, rgba(70,70,70,.8), rgba(70,70,70,0) 100%),
      linear-gradient(180deg, #9a9a9a 0%, #bcbcbc 35%, #8a8a8a 70%, #3a3a3a 100%);
  }
</style>
</head>
<body>
<main class="canvas">
  <span class="side-label side-label--a">Side A</span>
  <span class="side-label side-label--b">Side B</span>

  <section class="panel panel--front">
    <div class="photo" role="img" aria-label="Black and white photo of a mother kissing her smiling daughter on the cheek">
      <span class="photo-word">freedom</span>
    </div>
    <div class="hero-band">
      <svg class="hero-bars" viewBox="0 0 420 315" aria-hidden="true">
        <g fill="rgba(255,255,255,.10)">
          <rect x="50" y="270" width="40" height="45"/>
          <rect x="100" y="240" width="40" height="75"/>
          <rect x="150" y="205" width="40" height="110"/>
          <rect x="200" y="165" width="40" height="150"/>
          <rect x="250" y="120" width="40" height="195"/>
          <rect x="300" y="70" width="40" height="245"/>
        </g>
        <path d="M0 300 Q220 150 400 20" fill="none" stroke="rgba(255,255,255,.12)" stroke-width="14"/>
      </svg>
      <div class="hero-text">
        <p class="big">Be free</p>
        <p class="line">to live your life</p>
        <p class="small">and leave your</p>
        <p class="gold">bad credit worries</p>
        <p class="end">to us</p>
      </div>
    </div>
    <div class="brand">
      <div class="brand-row">
        <span class="brand-mark"></span>
        <span class="brand-name">TRV Credit</span>
      </div>
      <span class="brand-tagline">Raise your score. Raise your life!</span>
    </div>
    <address class="contact-band">
      4500 Harbor Lane, Suite B, Riverton, MD 21000<br>
      Email: office@trvcredit.com | Web: www.TRVCredit.com<br>
      Toll Free: (800)555-0142 | Local: (410)555-0187 | Fax: (800)555-0163
    </address>
  </section>

  <section class="panel panel--inside">
    <div class="message-band">
      <p class="lead">We will help you</p>
      <p class="strong">start over</p>
      <p class="gold">by sorting out</p>
      <p class="dark">your bad</p>
      <p class="end">credit</p>
    </div>
    <div class="photo" role="img" aria-label="Black and white photo of a mother and father tenderly holding their baby">
      <span class="photo-word">Security</span>
    </div>
  </section>
</main>
</body>
</html>
```